Hadley & Partners, LLC Business Card 2016

We need a new business card design for a very important trade show coming up.

We are a compliance Consulting Firm. Our clients are stock brokerage firms and investment advisers.

I would like our logo on both sides of the card.

Info in the front of the card shold include:

Logo
First & Last Name
Title
Office #
Cell #
Email
Company Address (42 W. Calloway St., Suite 300 Pasadena, CA 91417

Back of the card should include the logo and url: www.hadleypartnersgroup.com

Target Market(s)

Stock Brokerage Firms and Investment Advisers

Industry/Entity Type

Financial Service

Contact Information for Business Card

Marcus J. Pellew
President
42 W. Calloway St., Suite 300
Pasadena, CA 91417
O 626.555.0147 ext. 204
C 818.555.0193
Email: marcus@hadleypartnersgroup.com
www.hadleypartnersgroup.com

Requirements
Nice to have
• The back of the card could be black with the logo with the white letters.
• I do want the front of the card to at least have the color logo with the black "Hadley & Partners Lettering.

```html
<!DOCTYPE html>
<html lang="en">
<head>
<meta charset="utf-8">
<title>Hadley &amp; Partners, LLC — Business Card</title>
<link rel="stylesheet" href="https://fonts.googleapis.com/css2?family=Crimson+Text:wght@400;600&display=swap">
<style>
  :root {
    --stage: #e4e2e0;
    --card: #2a2627;
    --red: #d9342b;
    --white: #f2f0ee;
    --grey: #a9a4a2;
  }
  * { box-sizing: border-box; margin: 0; padding: 0; }
  html, body { width: 1200px; height: 813px; overflow: hidden; }
  body {
    background: var(--stage);
    font-family: "Crimson Text", Georgia, serif;
    display: flex;
    align-items: center;
    justify-content: center;
    gap: 48px;
  }
  .card {
    position: relative;
    width: 528px;
    height: 302px;
    background: var(--card);
    border-radius: 6px;
    box-shadow: 0 10px 28px rgba(0,0,0,.25);
    overflow: hidden;
    color: var(--white);
  }
  .brand {
    display: flex;
    align-items: center;
    gap: 12px;
    font-size: 27px;
    font-weight: 600;
    color: var(--white);
    white-space: nowrap;
  }
  .brand__mark { width: 30px; height: 30px; background: var(--red); flex: none; }

  /* front */
  .card--front .brand { position: absolute; top: 30px; right: 36px; }
  .holder { position: absolute; left: 40px; top: 98px; }
  .holder__name { font-size: 24px; letter-spacing: .04em; text-transform: uppercase; line-height: 1; }
  .holder__title { font-size: 20px; color: var(--red); line-height: 1.1; }
  .contacts {
    position: absolute; left: 40px; top: 162px;
    display: flex; gap: 10px;
  }
  .contacts__icons { display: flex; flex-direction: column; gap: 5px; padding-top: 2px; }
  .contacts__icons svg { width: 16px; height: 16px; display: block; }
  .contacts__rule { width: 2px; background: var(--red); }
  .contacts__list { list-style: none; font-size: 16px; line-height: 21px; color: var(--grey); }
  .address-band {
    position: absolute; left: 0; bottom: 26px;
    width: 470px; height: 38px;
    background: var(--red);
    border-radius: 0 8px 8px 0;
    display: flex; align-items: center;
    padding-left: 40px;
    font-size: 17px; color: var(--white);
  }

  /* back */
  .card--back .brand { position: absolute; left: 60px; top: 92px; font-size: 34px; }
  .card--back .brand__mark { width: 40px; height: 40px; }
  .web { position: absolute; left: 60px; top: 200px; font-size: 21px; color: var(--grey); }
  .web__domain { color: var(--red); }
</style>
</head>
<body>
  <section class="card card--front" aria-label="Card front">
    <div class="brand"><span class="brand__mark"></span>Hadley &amp; Partners</div>
    <div class="holder">
      <p class="holder__name">Marcus J. Pellew</p>
      <p class="holder__title">President</p>
    </div>
    <div class="contacts">
      <div class="contacts__icons">
        <svg viewBox="0 0 16 16" aria-label="Office"><circle cx="8" cy="8" r="8" fill="#d9342b"/><path d="M5 4.5l1.6-.6 1 2-1 .8c.5 1 1.2 1.7 2.2 2.2l.8-1 2 1-.6 1.6c-3 .2-6.2-3-6-6z" fill="#2a2627"/></svg>
        <svg viewBox="0 0 16 16" aria-label="Cell"><circle cx="8" cy="8" r="8" fill="#d9342b"/><rect x="5.6" y="3.5" width="4.8" height="9" rx="1" fill="#2a2627"/></svg>
        <svg viewBox="0 0 16 16" aria-label="Email"><circle cx="8" cy="8" r="8" fill="#d9342b"/><rect x="4" y="5.2" width="8" height="5.6" fill="#2a2627"/><path d="M4 5.2l4 3 4-3" stroke="#d9342b" stroke-width=".9" fill="none"/></svg>
      </div>
      <div class="contacts__rule"></div>
      <ul class="contacts__list">
        <li>626.555.0147 ext. 204</li>
        <li>818.555.0193</li>
        <li>marcus@hadleypartnersgroup.com</li>
      </ul>
    </div>
    <div class="address-band">42 W. Calloway St., Suite 300, Pasadena, CA 91417</div>
  </section>

  <section class="card card--back" aria-label="Card back">
    <div class="brand"><span class="brand__mark"></span>Hadley &amp; Partners</div>
    <p class="web">www.<span class="web__domain">hadleypartnersgroup</span>.com</p>
  </section>
</body>
</html>
```